Twitter Bootstrap Website Design (Gaming Themed)

I need a website designed using Twitter Bootstrap for a Rewards website. We'd like to see a gaming based design as the site will cater mostly to gamers.
This is a rewards site similar to sites like PerkNest
I only need the HTML/CSS design.
I need these pages:
1. Homepage for non-logged in users which will also have a sign up form
2. Homepage for logged in users
3. Profile Page
4. Rewards page which will display items that the user can redeem
a) A drop-down to sort by item category
5. Rewards page item details which will display a single item's details
6. About, FAQ, Terms Of Service Pages
Reason: Waiting for some more designs
Target Market(s)
13 to 30 year old gamers
Mostly males
Industry/Entity Type
It Service
Look and feel

```html
<!DOCTYPE html>
<html lang="en">
<head>
<meta charset="utf-8">
<title>Sitename Rewards</title>
<link rel="stylesheet" href="https://fonts.googleapis.com/css2?family=Aldrich&family=Lato:wght@300;400;700&family=Open+Sans:wght@700&display=swap">
<style>
  :root {
    --brand-blue: #2a53b5;
    --bar-dark: #333333;
    --footer-dark: #2e2e2e;
    --white: #ffffff;
    --connect-blue: #3b5998;
    --field-border: #cdd5df;
    --muted: #8c8c8c;
    --strip-text: #c9d3ec;
    --stat-text: #d0d0d0;
    --photo-dark: #1c1f26;
    --photo-mid: #4a4d55;
    --photo-light: #a9a6a1;
  }
  * { box-sizing: border-box; margin: 0; padding: 0; }
  html, body { width: 1200px; height: 882px; overflow: hidden; }
  body { position: relative; background: var(--footer-dark); font-family: "Lato", sans-serif; }

  .site-header { position: absolute; left: 0; top: 0; width: 1200px; height: 69px; background: var(--brand-blue); }
  .site-logo { position: absolute; left: 20px; top: 13px; font-family: "Aldrich", sans-serif; font-size: 37px; line-height: 40px; color: var(--white); letter-spacing: 1.5px; white-space: nowrap; }
  .auth-tab { position: absolute; top: 11px; height: 58px; width: 126px; font-family: "Aldrich", sans-serif; font-size: 17px; line-height: 62px; text-align: center; color: var(--white); }
  .auth-tab--idle { left: 921px; }
  .auth-tab--active { left: 1041px; background: var(--white); color: #222; border-radius: 8px 8px 0 0; }

  .main-nav { position: absolute; left: 0; top: 69px; width: 1200px; height: 33px; background: var(--bar-dark); }
  .main-nav a { position: absolute; top: 0; font-family: "Aldrich", sans-serif; font-size: 14px; line-height: 33px; color: #e6e6e6; text-decoration: none; letter-spacing: 0.5px; }

  .hero-photo { position: absolute; left: 0; top: 102px; width: 1200px; height: 647px;
    background:
      radial-gradient(ellipse 460px 360px at 320px 300px, var(--photo-light) 0%, rgba(169,166,161,0.45) 50%, transparent 85%),
      linear-gradient(100deg, var(--photo-mid) 0%, var(--photo-dark) 70%); }

  .signup-panel { position: absolute; left: 716px; top: 69px; width: 452px; height: 471px; background: var(--white); border-radius: 0 0 10px 10px; }
  .connect-button { position: absolute; left: 41px; top: 31px; width: 379px; height: 54px; padding-left: 36px; background: var(--connect-blue); border: 1px solid #2c4680; color: var(--white); font-size: 21px; font-weight: 700; line-height: 52px; text-align: center; white-space: nowrap; }
  .connect-button .mark { position: absolute; left: 11px; top: 12px; width: 28px; height: 28px; background: var(--white); }
  .divider { position: absolute; left: 41px; top: 98px; width: 379px; text-align: center; font-size: 15px; font-weight: 300; color: var(--muted); }
  .divider::before, .divider::after { content: ""; position: absolute; top: 10px; width: 66px; height: 1px; background: var(--field-border); }
  .divider::before { left: 0; } .divider::after { right: 0; }
  .field { position: absolute; left: 41px; width: 379px; height: 50px; border: 1px solid var(--field-border); border-radius: 2px; padding-left: 26px; font-family: "Lato", sans-serif; font-size: 16px; font-weight: 300; color: #333; background: var(--white); }
  .field::placeholder { color: var(--muted); }
  .legal { position: absolute; left: 45px; top: 331px; width: 370px; font-family: Arial, sans-serif; font-size: 11px; line-height: 15px; color: #555; }
  .start-button { position: absolute; left: 41px; top: 399px; width: 382px; height: 50px; background: var(--bar-dark); color: var(--white); font-size: 22px; font-weight: 700; line-height: 50px; text-align: center; border-radius: 2px; }

  .promo-strip { position: absolute; left: 0; top: 749px; width: 1200px; height: 32px; background: var(--brand-blue); font-family: "Aldrich", sans-serif; font-size: 16px; line-height: 33px; text-align: center; color: var(--strip-text); letter-spacing: 1.5px; white-space: nowrap; }
  .reward-total { position: absolute; left: 0; top: 781px; width: 1200px; height: 101px; background: var(--footer-dark); font-family: "Open Sans", sans-serif; font-weight: 700; font-size: 45px; line-height: 101px; text-align: center; color: var(--stat-text); white-space: nowrap; }
  .reward-total strong { font-size: 57px; color: var(--white); margin: 0 12px; }
</style>
</head>
<body>
  <header class="site-header">
    <div class="site-logo">SITENAME REWARDS</div>
    <div class="auth-tab auth-tab--idle">SIGN UP</div>
    <div class="auth-tab auth-tab--active">SIGN UP</div>
  </header>

  <nav class="main-nav">
    <a href="#" style="left:27px">HOME</a>
    <a href="#" style="left:154px">ABOUT US</a>
    <a href="#" style="left:320px">FAQ</a>
    <a href="#" style="left:433px">TERMS OF USE</a>
  </nav>

  <div class="hero-photo" role="img" aria-label="Photo of hands holding a white game controller in front of a blurred screen"></div>

  <section class="signup-panel">
    <div class="connect-button"><span class="mark"></span>Sign Up with Palvarra</div>
    <div class="divider">or sign up with your email below</div>
    <input class="field" style="top:135px" type="email" placeholder="Email Address">
    <input class="field" style="top:198px" type="password" placeholder="Password">
    <input class="field" style="top:260px" type="password" placeholder="Confirm Password">
    <p class="legal">By Signing up I agree to the Terms and Privacy Policy. I also agree to receive periodic emails with offers and promotional marketing messages from Sitename</p>
    <div class="start-button">Free. Get started</div>
  </section>

  <div class="promo-strip">START EARNING FREE GIFT CARDS TODAY</div>
  <div class="reward-total">Already has<strong>$48,324,509</strong>in Rewards</div>
</body>
</html>
```